VELTA CORE

I am in this industry for last 15 years we have done lots of commercial site like we work with BRAVEN costruction, lumo properties, TWD, penwick construction.
We do all domestic and commercial wall and floor tiling, swimming pools, spas, paving, marbles blue stones and muchmore.

Specializing in the wall and floor Tiling, Waterproofing and floor preparations

Industry/Entity Type

Industry

Number of Pages Required

1 page

Font styles to use
Serif
Decorative

Colors

Designer to choose colors to be used in the design.

Requirements
Must have
• domestic and commercial indoor tiling, bathroom tiling and paving pictures
Nice to have
• beautiful bathroom pictures with tile

```html
<!DOCTYPE html>
<html lang="en">
<head>
<meta charset="utf-8">
<title>VELTA CORE – Wall &amp; Floor Tiling</title>
<link href="https://fonts.googleapis.com/css2?family=Montserrat:wght@400;500;600;700&family=Open+Sans:wght@400;600&display=swap" rel="stylesheet">
<style>
:root{
  --green:#8ab31b;
  --green-light:#9cc23a;
  --teal:#3a8ea6;
  --ink:#1e1e1e;
  --body:#8a8a8a;
  --grey-panel:#6e6e6e;
  --footer:#1b1b1b;
  --white:#ffffff;
  --line:#e2e2e2;
}
*{margin:0;padding:0;box-sizing:border-box}
html,body{width:1200px;height:2866px;overflow:hidden;background:var(--white)}
body{position:relative;font-family:"Open Sans",sans-serif;color:var(--ink)}
.abs{position:absolute}
.btn{position:absolute;display:flex;align-items:center;justify-content:center;background:var(--teal);color:var(--white);font:600 13px "Montserrat",sans-serif;border-radius:14px;letter-spacing:.5px;text-transform:uppercase}

/* header */
.site-header{left:0;top:0;width:1200px;height:59px;background:var(--green)}
.brand{left:162px;top:17px;font:700 22px "Montserrat",sans-serif;color:var(--white);letter-spacing:.5px;white-space:nowrap}
.nav-link{position:absolute;top:24px;font:600 11px "Montserrat",sans-serif;color:var(--white);text-transform:uppercase;white-space:nowrap}
.nav-link.active{border-bottom:2px solid var(--white);padding-bottom:5px}
.search{left:828px;top:19px;width:106px;height:21px;display:flex}
.search span{flex:1;background:var(--white);font-size:9px;color:#aaa;padding:5px 6px}
.search i{width:18px;background:#53c3d8}

/* hero */
.hero{left:0;top:59px;width:1200px;height:530px}
.hero-photo{width:1200px;height:530px;background:linear-gradient(100deg,#8fb497 0%,#a8c9a6 35%,#6fa39c 60%,#3c6e6a 80%,#6b4a36 100%)}
.hero-shade{left:0;top:0}
.hero-title{left:204px;top:334px;font:500 38px "Montserrat",sans-serif;color:var(--white);letter-spacing:1px;white-space:nowrap}
.hero-text{left:160px;top:393px;width:440px;text-align:center;font-size:11.5px;line-height:16px;color:#e8e8e8}

/* sections */
.section-title{width:1200px;left:0;text-align:center;font:500 28px "Montserrat",sans-serif;color:var(--ink)}
.section-title b{color:var(--green);font-weight:500}
.title-rule{left:569px;width:62px;height:2px;background:var(--ink)}

.about-title{left:162px;top:664px;font:500 28px "Montserrat",sans-serif}
.about-rule{left:162px;top:704px;width:78px;height:2px;background:var(--ink)}
.about-text{left:162px;top:719px;font-size:12px;line-height:24px;color:var(--body);white-space:nowrap}
.about-photo{left:460px;top:694px}

.projects{left:160px;top:1256px}
.project-label{font:600 10px "Montserrat",sans-serif;color:var(--white);top:1480px}

.product-card{top:1794px;width:203px;height:474px;border:1px solid var(--line);background:var(--white)}
.product-card .photo{height:147px}
.product-card h3{height:37px;background:var(--green-light);color:var(--white);font:600 15px "Montserrat",sans-serif;text-align:center;line-height:37px;text-transform:uppercase}
.product-card p{padding:20px 14px 0;text-align:center;font-size:10.5px;line-height:17px;color:var(--body)}
.product-card .btn{left:43px;top:412px;width:116px;height:27px}

/* footer */
.map{left:0;top:2312px;width:600px;height:488px;background:linear-gradient(160deg,#e6eadf 0%,#d9e5c6 40%,#eef0ea 60%,#9cc6ea 85%,#8fbde7 100%)}
.contact{left:600px;top:2312px;width:600px;height:488px;background:var(--grey-panel);color:var(--white)}
.contact h2{position:absolute;left:178px;top:74px;font:500 22px "Montserrat",sans-serif;text-transform:uppercase}
.contact-item{position:absolute;left:178px;display:flex;gap:16px;align-items:center;font:500 13px "Montserrat",sans-serif}
.contact-item small{display:block;font-size:11px;text-transform:uppercase}
.follow{position:absolute;left:162px;top:334px;font:500 14px "Montserrat",sans-serif}
.socials{position:absolute;left:162px;top:371px;display:flex;gap:6px}
.socials span{width:50px;height:50px;border-radius:50%;border:2px solid var(--white)}
.site-footer{left:0;top:2800px;width:1200px;height:66px;background:var(--footer);color:#cfcfcf;font-size:12px;padding:24px 162px}
</style>
</head>
<body>

<header class="abs site-header">
  <div class="abs brand">VELTA CORE</div>
  <nav>
    <span class="nav-link active" style="left:317px">Home</span>
    <span class="nav-link" style="left:380px">About Us</span>
    <span class="nav-link" style="left:464px">Our Project</span>
    <span class="nav-link" style="left:571px">Product</span>
    <span class="nav-link" style="left:653px">Blogs</span>
    <span class="nav-link" style="left:717px">Contact Us</span>
  </nav>
  <div class="abs search"><span>Search...</span><i></i></div>
</header>

<section class="abs hero">
  <div class="hero-photo" role="img" aria-label="Green tiled bathroom with sunken pool and lounge chair"></div>
  <svg class="abs hero-shade" width="1200" height="530" viewBox="0 0 1200 530">
    <polygon points="0,266 535,266 669,530 0,530" fill="rgba(0,0,0,0.62)"/>
  </svg>
  <div class="abs hero-title">LOREM IPSUM IS</div>
  <p class="abs hero-text">Lorem Ipsum is simply dummy text of the printing and typesetting industry. Lorem Ipsum is simply dummy text of the printing and typesetting industry Lorem Ipsum is simply dummy .</p>
  <div class="btn" style="left:317px;top:455px;width:117px;height:25px">More</div>
</section>

<h2 class="abs about-title">ABOUT US</h2>
<div class="abs about-rule"></div>
<p class="abs about-text">Lorem Ipsum is simply dummy text of the printing<br>and typesetting industry. Lorem Ipsum has been the<br>industry's standard dummy text ever since the 1500s,<br>when an unknown printer took a galley of type and scra<br>mbled it to make, Lorem Ipsum .<br>is simply dummy text of the printing and typesetting industry.<br>Lorem Ipsum has been the industry's standard dummy text<br>ever since the 1500s, when an unknown printer took a galley of type<br>and scrambled it to make .</p>
<div class="btn" style="left:162px;top:950px;width:117px;height:27px">Read More</div>
<svg class="abs about-photo" width="578" height="260" viewBox="0 0 578 260" role="img" aria-label="Bright marble bathroom with glass shower">
  <defs><linearGradient id="aboutTone" x1="0" x2="1"><stop offset="0" stop-color="#6b6a5e"/><stop offset=".5" stop-color="#d8d6d0"/><stop offset="1" stop-color="#8f8c86"/></linearGradient></defs>
  <polygon points="0,0 578,0 578,260 210,260" fill="url(#aboutTone)"/>
</svg>

<h2 class="abs section-title" style="top:1127px">OUR <b>PROJECTS</b></h2>
<div class="abs title-rule" style="top:1177px"></div>
<svg class="abs projects" width="878" height="259" viewBox="0 0 878 259" role="img" aria-label="Three finished bathroom tiling projects">
  <defs>
    <linearGradient id="p1" x1="0" x2="1"><stop offset="0" stop-color="#5a3a22"/><stop offset="1" stop-color="#a58b6e"/></linearGradient>
    <linearGradient id="p2" x1="0" x2="1"><stop offset="0" stop-color="#2a2a2a"/><stop offset=".5" stop-color="#8a8a8a"/><stop offset="1" stop-color="#3a3a3a"/></linearGradient>
    <linearGradient id="p3" x1="0" x2="1"><stop offset="0" stop-color="#3b342e"/><stop offset="1" stop-color="#6e6e78"/></linearGradient>
  </defs>
  <polygon points="0,0 208,0 298,259 0,259" fill="url(#p1)"/>
  <polygon points="208,0 566,0 671,259 298,259" fill="url(#p2)"/>
  <polygon points="566,0 878,0 878,259 671,259" fill="url(#p3)"/>
  <rect x="0" y="219" width="878" height="21" fill="rgba(0,0,0,0.55)"/>
  <line x1="208" y1="0" x2="298" y2="259" stroke="#fff" stroke-width="9"/>
  <line x1="566" y1="0" x2="671" y2="259" stroke="#fff" stroke-width="9"/>
</svg>
<span class="abs project-label" style="left:170px">LOREM IPSAM</span>
<span class="abs project-label" style="left:474px">LOREM IPSAM</span>
<span class="abs project-label" style="left:840px">LOREM IPSAM</span>

<h2 class="abs section-title" style="top:1675px">OUR <b>PRODUCTS</b></h2>
<div class="abs title-rule" style="top:1725px"></div>

<article class="abs product-card" style="left:160px">
  <div class="photo" role="img" aria-label="Grey wall tiles in a modern bathroom" style="background:linear-gradient(135deg,#3c3c3c,#a8a8a8)"></div>
  <h3>Wall Tiles</h3>
  <p>Lorem Ipsum is simply dummy text of the printing and type-setting industry. Lorem Ipsum has been the industry's stan-dard dummy text ever since the 1500s, when an unknown printer took a galley of type and scrambled it to make a type specimen book. It has</p>
  <div class="btn">Read More</div>
</article>
<article class="abs product-card" style="left:386px">
  <div class="photo" role="img" aria-label="Polished wooden-look floor tiles" style="background:linear-gradient(170deg,#2a1a0c,#c08a45 60%,#6b3f1a)"></div>
  <h3>Floor Tiles</h3>
  <p>Lorem Ipsum is simply dummy text of the printing and type-setting industry. Lorem Ipsum has been the industry's stan-dard dummy text ever since the 1500s, when an unknown printer took a galley of type and scrambled it to make a</p>
  <div class="btn">Read More</div>
</article>
<article class="abs product-card" style="left:612px">
  <div class="photo" role="img" aria-label="Marble floor in a bright lobby" style="background:linear-gradient(160deg,#6d5a48,#c9b4a0 55%,#8b6e58)"></div>
  <h3>Floor Merbel</h3>
  <p>Lorem Ipsum is simply dummy text of the printing and type-setting industry. Lorem Ipsum has been the industry's stan-dard dummy text ever since the 1500s, when an unknown printer took a galley of type and scrambled it to make a type specimen book. It has survived not only five centuries, but also the leap into electron-</p>
  <div class="btn">Read More</div>
</article>
<article class="abs product-card" style="left:837px">
  <div class="photo" role="img" aria-label="Waterproofing plans and tools on a table" style="background:linear-gradient(150deg,#c8ccd2,#8fa1b8 50%,#e4e4e0)"></div>
  <h3>Waterproof</h3>
  <p>Lorem Ipsum is simply dummy text of the printing and type-setting industry. Lorem Ipsum has been the industry's stan-dard dummy text ever since the 1500s, when an unknown printer took a galley of type and scrambled it to make a type specimen book. It has</p>
  <div class="btn">Read More</div>
</article>

<div class="abs map" role="img" aria-label="Map showing the office location on the coast"></div>
<section class="abs contact">
  <h2>Contact Us</h2>
  <div class="contact-item" style="top:131px">
    <svg width="14" height="18" viewBox="0 0 14 18"><path d="M7 0a7 7 0 0 0-7 7c0 5 7 11 7 11s7-6 7-11a7 7 0 0 0-7-7zm0 10a3 3 0 1 1 0-6 3 3 0 0 1 0 6z" fill="#111"/></svg>
    <div><small>Head Office</small>12 Harlow St, 4021</div>
  </div>
  <div class="contact-item" style="top:202px">
    <svg width="20" height="14" viewBox="0 0 20 14"><rect x="1" y="1" width="18" height="12" fill="none" stroke="#111" stroke-width="2"/><path d="M1 1l9 7 9-7" fill="none" stroke="#111" stroke-width="2"/></svg>
    <span>hello@veltacore.com</span>
  </div>
  <div class="contact-item" style="top:253px">
    <svg width="16" height="16" viewBox="0 0 16 16"><path d="M3 0l3 4-2 2c1 2 4 5 6 6l2-2 4 3-2 3C7 16 0 9 0 3z" fill="#111"/></svg>
    <span>555-010-2040</span>
  </div>
  <div class="follow">Follow us:</div>
  <div class="socials"><span></span><span></span><span></span><span></span><span></span></div>
</section>

<footer class="abs site-footer">&copy;All Rights Reserved 2017</footer>

</body>
</html>
```